BUSINESS CARD DESIGN FOR CONSULTING BUSINESS

I need a business card design containing my logo and slogan for my new consulting business. The consulting business provides the following services: 1) human resource services assistance (payroll, expert advice, developing strategic and recruitment plans and blogs) for small businesses and 2) develops content for small business blogs and online magazines. I plan to expand the business, so I don't want to focus on the services but rather on my initials (LT) for name recognition and the name of the company, Dunmore Advisory Services.
My slogan is Relevant, Innovative, Expert Solutions.
I want a business card that is plain and not busy and contains a logo that reflects my work: consulting and writing. I would also like the business card to include the following contact information in this order: Lena Tolliver, Principal (lst line) Sr. Consultant (2nd line), 4730 Pellman Street, #502317, Sacramento, CA 95824, (3rd line) ltolliveradvisory@quillpost.net, (4th line), (916) 555-0172 (5th line), (my name, title, business address, email address, and phone number). My business's logo and name, Dunmore Advisory Services, should appear next to each other on the front of the card. The slogan should also be noted on the back of the card. Thanks!

Target Market(s)

Small businesses and governments.

Industry/Entity Type

Human Resources (HR) and Writing, but please focus on consulting services which can be both (HR and writing) or neither.

Logo Text

If possible, please create a abstract logo like the attachment. Or create a logo using my first and last initials (LT) and the word consulting like the Rupert Vane (RV) example below.

Logo styles of interest
Abstract Logo
Wordmark Logo
Lettermark Logo
Font styles to use
Serif

Colors

Designer to choose colors to be used in the design.

Requirements
Must have
• Please feel free to create your own design as the attachment is just an example to show that I prefer a simple design with that format/layout if possible. The logo should be simple like a lettermark, word mark or abstract logo with the logo on the front and the slogan on the back. Please note my contact information in this order: my name with a title of Principal/Sr. Consultant, my address, email address and my phone number..
Nice to have
• Please see the attached sample design. A blue, or green or blue violet color card may look great. I am also good with simple black and white. Thanks!
Should not have
• Large, busy logo

```html
<!DOCTYPE html>
<html lang="en">
<head>
<meta charset="utf-8">
<title>Lena Tolliver — Dunmore Advisory Services business cards</title>
<link rel="stylesheet" href="https://fonts.googleapis.com/css2?family=Oswald:wght@500&family=Montserrat:wght@300&family=Barlow:wght@400;600&display=swap">
<style>
  :root {
    --purple: #6a4c8c;
    --purple-dark: #3a2c45;
    --purple-mid: #5a4178;
    --green: #a6c64c;
    --grey-text: #6f6f6f;
    --stage: #d4d4d4;
    --stage-dark: #b3b3b3;
    --white: #ffffff;
    --card-white: #f7f7f8;
  }
  * { margin: 0; padding: 0; box-sizing: border-box; }
  html, body { width: 1200px; height: 971px; overflow: hidden; }
  body { font-family: "Barlow", Arial, sans-serif; background: var(--white); position: relative; }

  .stage {
    position: absolute; left: 0; top: 0; width: 1200px; height: 686px;
    background: radial-gradient(ellipse at 35% 0%, #f4f4f4 0%, var(--stage) 55%, var(--stage-dark) 100%);
  }
  .card {
    position: absolute; top: 190px; width: 520px; height: 297px;
    box-shadow: 0 10px 24px rgba(0,0,0,0.22);
  }
  .card--back { left: 50px; background: linear-gradient(120deg, #6f5396 0%, var(--purple-mid) 45%, var(--purple-dark) 100%); }
  .card--front { left: 630px; background: var(--card-white); }

  /* lockup */
  .lockup { position: absolute; display: flex; align-items: center; }
  .lockup__mark { width: 34px; height: 34px; background: var(--purple); margin-right: 14px; }
  .lockup__name { font-family: "Oswald", "Arial Narrow", sans-serif; font-weight: 500; font-size: 34px; letter-spacing: 0.01em; color: var(--purple); line-height: 1; transform: scaleX(0.85); transform-origin: left center; margin-right: -30px; }
  .lockup__rule { width: 1px; height: 44px; background: var(--purple); margin: 0 10px; }
  .lockup__tagline { font-family: "Montserrat", Arial, sans-serif; font-weight: 300; font-size: 7.5px; letter-spacing: 0.42em; line-height: 1.45; color: var(--green); text-transform: uppercase; }

  .card--back .lockup { left: 100px; top: 126px; }
  .card--back .lockup__mark { background: var(--white); }
  .card--back .lockup__name { color: var(--white); }
  .card--back .lockup__rule { background: var(--white); }

  .card--front .lockup { left: 40px; top: 46px; }

  .contact { position: absolute; left: 260px; top: 150px; width: 230px; color: var(--grey-text); font-size: 10px; line-height: 1.35; }
  .contact__name { color: var(--purple); font-weight: 600; font-size: 13px; line-height: 1.1; }
  .contact__title { font-size: 10px; margin-bottom: 10px; }
  .contact__rule { height: 1px; background: var(--purple); margin: 6px 0 6px; }
  .contact__label { color: var(--purple); font-weight: 600; }

  .web { position: absolute; left: 40px; bottom: 28px; color: var(--grey-text); }
  .web__url { font-size: 13px; letter-spacing: 0.02em; margin-bottom: 6px; }
  .web__social { display: flex; align-items: center; font-size: 9.5px; }
  .web__dot { width: 10px; height: 10px; border-radius: 50%; background: var(--purple); margin-right: 6px; }

  /* presentation lockup */
  .brand {
    position: absolute; left: 0; top: 686px; width: 1200px; height: 285px;
    display: flex; align-items: center; justify-content: center;
  }
  .brand .lockup { position: static; }
  .brand .lockup__mark { width: 96px; height: 96px; margin-right: 34px; }
  .brand .lockup__name { font-size: 100px; margin-right: -96px; }
  .brand .lockup__rule { height: 124px; width: 2px; margin: 0 18px; }
  .brand .lockup__tagline { font-size: 21px; letter-spacing: 0.4em; line-height: 1.38; }
</style>
</head>
<body>
  <div class="stage">
    <section class="card card--back" aria-label="Business card back">
      <div class="lockup">
        <div class="lockup__mark"></div>
        <div class="lockup__name">LENA TOLLIVER</div>
        <div class="lockup__rule"></div>
        <div class="lockup__tagline">Dunmore<br>Advisory<br>Services</div>
      </div>
    </section>

    <section class="card card--front" aria-label="Business card front">
      <div class="lockup">
        <div class="lockup__mark"></div>
        <div class="lockup__name">LENA TOLLIVER</div>
        <div class="lockup__rule"></div>
        <div class="lockup__tagline">Dunmore<br>Advisory<br>Services</div>
      </div>

      <div class="contact">
        <p class="contact__name">Lena Tolliver</p>
        <p class="contact__title">Sr. Consultant</p>
        <p>4730 Pellman Street, #502317, Sacramento, CA 95824</p>
        <div class="contact__rule"></div>
        <p><span class="contact__label">e-mail :</span> ltolliveradvisory@quillpost.net</p>
        <p><span class="contact__label">celular :</span> (916) 555-0172</p>
      </div>

      <div class="web">
        <p class="web__url">www.lenatolliver.com</p>
        <p class="web__social"><span class="web__dot"></span>/dunmoreadvisoryservices</p>
      </div>
    </section>
  </div>

  <div class="brand">
    <div class="lockup">
      <div class="lockup__mark"></div>
      <div class="lockup__name">LENA TOLLIVER</div>
      <div class="lockup__rule"></div>
      <div class="lockup__tagline">Dunmore<br>Advisory<br>Services</div>
    </div>
  </div>
</body>
</html>
```